RTV ELECTRICAL GROUP Website Providing Electrical Services

We're a company providing electrical services to the public. We're located in Bankstown a suburb in Sydney, Australia. We are a team of 4 electricians that provide service work to the public. We work on new construction buildings such as single story, double story & units. We also do office fit outs & commercial factory work.

Target Market(s)

All Age Groups
Construction People
Sydney, Australia

Industry/Entity Type

Electrical

Contact Information for Business Card

Name Gavin Lorrimer
Contact Number 0481 502 743
Company License 904517B
ABN 53 204 871 365
Residential Commercial Industrial
info@rtvelectrical.example.com.au

Coding

Coded - Design and coding required

Number of Pages Required

5+ page

Font styles to use
Serif
Sans Serif

Colors

Designer to choose colors to be used in the design.

Requirements
Must have
• WORDPRESS
• Nice & Simple
• Eye catching
• Easy to Read
• Contact details
• Instagram Linked
• Facebook Page Linked
• All Social Media Linked
• Live Chat
• Form Submission
• Testimonial
• Specify services Offered
• About Us (Company details)
• Industrial Installation Page
• Residential Installation Page
• Commercial Installation Page
• Mode of payment (cash, credit-debit card, cheque)
• Local & national electrical news
• Project Videos
• Newsletter
• Level 2 licensed accredited
• Project pictures and articles
• Awards
• Legalities (company's policy, terms, rules)
• FAQ's (Frequently asked questions)
• Collaboration Projects
• Careers
• Projects
• Suppliers
• Customer Perks (discounts or freebies)
• Employees Informations (pictures and basic information)
• Opening Hours and Map location
• Company Logo & Company License (owner license)
• Accreditation
• Customer Service
• Safety/Safety tips
• Clients information (regular clients)
• Expertise
• Company's processes
• Timeline page
• Homepage
• Specify installations
• Search toolbar
• Portfolio
• Request for an appointment - servicing
• Feedbacks
Nice to have
• Articles (better if recent project articles)
• Advertisement
• Influencer Quote
• Sneak Peeks (if you have new services offered)
• Staff Highlights
• Job Hiring (Career Growth)
• Ratings (Rate our service)
• A day/week in the work
• Personal Anecdotes
• Before and after post projects
• Ecological Values
• Marketing feature
• Tagline
• Streaming interactive videos
• Timeline
• Calendar
• Blog
• Emergency Services/Hotline
• Additional services offered
• Transportation (vehicle - car images of our company)
• Comment box (company - clients)
• Rate Us (Performance rating)
Should not have
• Website shouldn't be dark
• Website shouldn't be hard to read
• Advertisement of competitors
• Moving objects
• Dark background

```html
<!DOCTYPE html>
<html lang="en">
<head>
<meta charset="utf-8">
<title>RTV Electrical Group – Electrical Services Sydney</title>
<link rel="stylesheet" href="https://fonts.googleapis.com/css2?family=Open+Sans:wght@400;600;700&family=Montserrat:wght@500;600;700&display=swap">
<style>
:root{
  --blue:#0d5a9e;
  --blue-light:#1d7cc4;
  --blue-dark:#0a4478;
  --ink:#222;
  --text:#444;
  --muted:#777;
  --nav:#3c3c3c;
  --footer:#363636;
  --soft:#f3f3f3;
  --line:#ddd;
  --white:#fff;
}
*{box-sizing:border-box;margin:0;padding:0}
html,body{width:1200px;height:4700px;overflow:hidden}
body{font-family:"Open Sans",Arial,sans-serif;color:var(--text);background:var(--white);position:relative}
.abs{position:absolute}
h2.section-title{font-family:"Montserrat",Arial,sans-serif;font-weight:600;font-size:27px;letter-spacing:1px;color:var(--ink);text-align:center}
.section-sub{font-size:13px;font-weight:600;text-align:center;color:var(--ink);line-height:18px}
.btn{display:inline-block;border:2px solid var(--ink);border-radius:4px;font-size:14px;font-weight:700;color:var(--ink);padding:6px 26px;background:var(--white)}
.center-btn{position:absolute;left:0;width:1200px;text-align:center}
.dots{position:absolute;left:0;width:1200px;text-align:center}
.dots i{display:inline-block;width:7px;height:7px;border-radius:50%;background:#333;margin:0 3px}
.dots i.dim{background:#8aa8c8}

/* header */
.topbar{top:0;left:0;width:1200px;height:135px}
.topbar .contact{top:48px;display:flex;align-items:center;gap:12px;font-size:14px;font-weight:600;color:var(--ink);line-height:18px}
.icon-circle{width:38px;height:38px;border-radius:50%;background:var(--blue);display:flex;align-items:center;justify-content:center}
.brand{top:30px;left:0;width:1200px;text-align:center}
.brand .mark{width:34px;height:34px;border-radius:50%;background:var(--blue);margin:0 auto 10px}
.brand .name{font-family:"Montserrat",Arial,sans-serif;font-weight:600;font-size:18px;letter-spacing:1px;color:var(--blue)}
.call .label{color:var(--blue);font-weight:700}
.nav{top:135px;left:0;width:1200px;height:45px;background:var(--nav)}
.nav ul{list-style:none;display:flex;position:absolute;left:118px;top:0;height:45px}
.nav li{font-family:"Montserrat",Arial,sans-serif;font-size:13px;font-weight:600;color:var(--white);padding:0 26px;line-height:45px}
.nav li.active{background:#555}
.nav .quote{position:absolute;right:115px;top:0;height:45px;line-height:45px;background:var(--blue);color:var(--white);font-family:"Montserrat",Arial,sans-serif;font-size:13px;font-weight:600;padding:0 20px}

/* hero */
.hero{top:180px;left:0;width:1200px;height:525px;background:linear-gradient(100deg,#5a5f63 0%,#8d8f8c 30%,#b7b4ae 55%,#9a8c7c 75%,#6d6a66 100%)}
.hero .shade{position:absolute;inset:0;background:linear-gradient(180deg,rgba(0,0,0,0) 40%,rgba(0,0,0,.35) 100%)}
.hero .arrow{position:absolute;top:215px;width:30px;height:30px;background:rgba(40,40,40,.8);display:flex;align-items:center;justify-content:center}
.hero .caption{position:absolute;left:0;top:218px;width:1200px;text-align:center;color:var(--white)}
.hero h1{font-family:"Open Sans",Arial,sans-serif;font-weight:700;font-variant:small-caps;font-size:25px;letter-spacing:1px}
.hero p{font-size:15px;font-weight:700;margin-top:2px}
.hero .btn{background:#222;border-color:#fff;color:#fff;margin-top:18px;font-size:13px;padding:5px 22px}

/* about */
.about{top:715px;left:0;width:1200px;height:445px;background:linear-gradient(135deg,#f6f6f6,#ececec)}
.about h2{position:absolute;left:118px;top:105px;font-family:"Montserrat",Arial,sans-serif;font-size:26px;font-weight:600;color:var(--ink)}
.about .rule{position:absolute;left:118px;top:140px;width:70px;height:3px;background:var(--ink)}
.about .copy{position:absolute;left:118px;top:158px;width:470px;font-size:13px;font-weight:600;color:var(--ink);line-height:17px}
.about ul{margin-top:14px;list-style:none}
.about li{line-height:23px}
.about li::before{content:"";display:inline-block;width:6px;height:6px;background:var(--ink);border-radius:50%;margin-right:10px;vertical-align:middle}
.about .btn{position:absolute;left:118px;top:345px;padding:4px 36px;font-size:13px}
.about .photo{position:absolute;left:615px;top:90px;width:465px;height:265px;background:linear-gradient(135deg,#d9dadb,#a9b7c4 45%,#5f89b3 70%,#c9ccce)}
.about .thumbs{position:absolute;left:615px;top:355px;width:465px;height:18px;display:flex;gap:4px}
.about .thumbs span{flex:1;background:#2d2d2d}
.about .thumbs span.on{background:var(--blue)}

/* services */
.services{top:1160px;left:0;width:1200px;height:740px}
.services h2{position:absolute;top:65px;left:0;width:1200px}
.services .section-sub{position:absolute;top:105px;left:0;width:1200px}
.svc-grid{position:absolute;left:118px;top:190px;width:965px;display:grid;grid-template-columns:repeat(3,1fr);row-gap:18px}
.svc{height:190px;text-align:center;padding-top:18px}
.svc.hl{background:#f1f1f1}
.svc svg{width:50px;height:50px}
.svc h3{font-family:"Montserrat",Arial,sans-serif;font-size:15px;font-weight:600;color:var(--ink);margin-top:8px;letter-spacing:.5px}
.svc p{font-size:12px;color:var(--text);line-height:15px;margin-top:4px}
.svc .more{font-size:12px;font-weight:600;color:var(--ink);margin-top:6px}
.services .center-btn{top:635px}

/* benefits */
.benefits{top:1905px;left:0;width:1200px;height:440px;background:linear-gradient(90deg,#0b4f8d 0%,#1466ad 50%,#0d5699 100%)}
.benefits h2{position:absolute;left:116px;top:95px;font-family:"Montserrat",Arial,sans-serif;font-size:29px;font-weight:600;color:var(--white)}
.benefits h4{position:absolute;left:116px;top:137px;font-size:17px;font-weight:600;color:var(--white)}
.benefits p{position:absolute;left:116px;top:172px;width:470px;font-size:13px;font-weight:700;color:var(--white);line-height:17px}
.benefits .btn{position:absolute;left:116px;top:320px;background:var(--blue-dark);border-color:var(--white);color:var(--white);padding:5px 36px;font-size:13px}
.benefits .photo{position:absolute;left:615px;top:40px;width:465px;height:360px;background:linear-gradient(135deg,#f2f2f2,#dcdcdc 45%,#e8a17a 65%,#e24a2c 75%,#d8d8d8)}

/* testimonials */
.testimonials{top:2345px;left:0;width:1200px;height:630px}
.testimonials h2{position:absolute;top:70px;left:0;width:1200px}
.testimonials .section-sub{position:absolute;top:103px;left:0;width:1200px;font-weight:400;font-size:12px}
.card{position:absolute;background:#f7f7f7;box-shadow:0 2px 8px rgba(0,0,0,.18);text-align:center}
.card .avatar{width:96px;height:96px;border-radius:50%;background:linear-gradient(180deg,#b9bfc6,#5d6670);margin:22px auto 8px;border:3px solid #fff}
.card h5{font-size:16px;font-weight:400;color:var(--ink)}
.card .role{font-size:12px;color:var(--blue);font-weight:600}
.card .quote{position:relative;padding:8px 46px 0;font-size:12px;color:var(--text);line-height:15px}
.card .quote b{position:absolute;font-family:Georgia,serif;font-size:30px;color:var(--ink);line-height:1}
.card .more{font-size:12px;color:var(--text);margin-top:12px}
.testimonials .dots{top:518px}
.testimonials .center-btn{top:568px}

/* blogs */
.blogs{top:2975px;left:0;width:1200px;height:535px;background:#f4f4f4}
.blogs h2{position:absolute;top:35px;left:0;width:1200px}
.blogs .section-sub{position:absolute;top:70px;left:0;width:1200px;font-weight:400;font-size:12px}
.post{position:absolute;top:110px;width:305px}
.post .img{height:195px;position:relative}
.post .date{position:absolute;left:0;top:0;width:36px;height:36px;background:#222;color:#fff;font-size:11px;font-weight:700;text-align:center;line-height:14px;padding-top:4px}
.post h6{font-size:13px;font-weight:600;color:var(--ink);margin-top:14px}
.post .meta{font-size:11px;color:var(--muted);margin-top:3px;display:flex;justify-content:space-between}
.post p{font-size:13px;color:var(--ink);line-height:16px;margin-top:8px}
.post .more{font-size:12px;color:var(--ink);margin-top:8px}
.blogs .center-btn{top:450px}

/* team */
.team{top:3510px;left:0;width:1200px;height:560px}
.team h2{position:absolute;top:50px;left:0;width:1200px}
.member{position:absolute;top:95px;width:200px;text-align:center}
.member .img{width:170px;height:265px;margin:0 auto;background:linear-gradient(180deg,#f0f0f0 0%,#bfc3c7 35%,#7b7f83 65%,#e3e3e3 100%)}
.member h5{font-size:14px;font-weight:400;color:var(--ink);margin-top:14px}
.member .role{font-size:12px;color:var(--text)}
.member .social{margin-top:6px}
.member .social i{display:inline-block;width:11px;height:11px;border-radius:50%;background:#222;margin:0 2px}
.team .center-btn{top:485px}

/* newsletter */
.newsletter{top:4070px;left:0;width:1200px;height:205px}
.newsletter h2{position:absolute;top:15px;left:0;width:1200px;font-size:24px}
.newsletter .section-sub{position:absolute;top:50px;left:0;width:1200px;font-weight:400;letter-spacing:1px}
.newsletter form{position:absolute;left:305px;top:105px;display:flex}
.newsletter .field{width:445px;height:26px;border:1px solid var(--line);font-size:11px;color:var(--muted);padding:5px 8px}
.newsletter .submit{width:100px;height:26px;background:var(--blue);color:#fff;font-size:13px;font-weight:700;text-align:center;line-height:26px;letter-spacing:1px}

/* footer */
.footer{top:4275px;left:0;width:1200px;height:395px;background:var(--footer);color:var(--white)}
.footer .brand{top:30px}
.footer .brand .mark{background:var(--white)}
.footer .brand .name{color:var(--white)}
.footer .tag{position:absolute;top:120px;left:0;width:1200px;text-align:center;font-size:13px;font-weight:700}
.footer .social{position:absolute;top:148px;left:0;width:1200px;text-align:center}
.footer .social i{display:inline-block;width:16px;height:16px;border-radius:50%;background:var(--white);margin:0 3px}
.fcol{position:absolute;top:200px;width:300px;text-align:center}
.fcol .ic{width:40px;height:40px;border-radius:50%;background:var(--white);margin:0 auto;display:flex;align-items:center;justify-content:center}
.fcol h6{font-size:15px;font-weight:700;margin-top:12px;letter-spacing:.5px}
.fcol p{font-size:12px;margin-top:4px}
.bottombar{top:4670px;left:0;width:1200px;height:30px;background:var(--blue)}
.bottombar .legal{position:absolute;left:118px;top:7px;font-size:12px;font-weight:600;color:#fff}
.bottombar .chat{position:absolute;right:40px;top:2px;height:28px;width:110px;background:var(--blue-light);color:#fff;font-size:13px;font-weight:700;line-height:28px;text-align:center;border-radius:4px 4px 0 0}
</style>
</head>
<body>

<header class="abs topbar">
  <div class="abs contact" style="left:118px">
    <div class="icon-circle"><svg width="16" height="20" viewBox="0 0 16 20"><path d="M8 0C3.6 0 0 3.5 0 7.8 0 13.5 8 20 8 20s8-6.5 8-12.2C16 3.5 12.4 0 8 0z" fill="#fff"/><circle cx="8" cy="7.8" r="3" fill="#0d5a9e"/></svg></div>
    <div>5234 West Harlow<br>Sydney, Australia , zip</div>
  </div>
  <div class="abs brand">
    <div class="mark"></div>
    <div class="name">RTV ELECTRICAL GROUP</div>
  </div>
  <div class="abs contact call" style="left:928px">
    <div class="icon-circle"><svg width="18" height="18" viewBox="0 0 24 24"><path d="M6.6 10.8a15.1 15.1 0 0 0 6.6 6.6l2.2-2.2c.3-.3.7-.4 1-.2 1.1.4 2.3.6 3.6.6.6 0 1 .4 1 1V20c0 .6-.4 1-1 1A17 17 0 0 1 3 4c0-.6.4-1 1-1h3.5c.6 0 1 .4 1 1 0 1.3.2 2.5.6 3.6.1.3 0 .7-.2 1z" fill="#fff"/></svg></div>
    <div><span class="label">CALL US NOW</span><br>+000 123 4567</div>
  </div>
</header>

<nav class="abs nav">
  <ul>
    <li class="active">HOME</li><li>ABOUT US</li><li>SERVICES</li><li>BLOG</li><li>CONTACT</li>
  </ul>
  <div class="quote">GET A QUOTE</div>
</nav>

<section class="abs hero">
  <div role="img" aria-label="Electrician in a hard hat working on a switchboard" style="position:absolute;inset:0"></div>
  <div class="shade"></div>
  <div class="arrow" style="left:40px"><svg width="10" height="12" viewBox="0 0 10 12"><path d="M8 1 2 6l6 5" stroke="#fff" stroke-width="2" fill="none"/></svg></div>
  <div class="arrow" style="right:40px"><svg width="10" height="12" viewBox="0 0 10 12"><path d="M2 1l6 5-6 5" stroke="#fff" stroke-width="2" fill="none"/></svg></div>
  <div class="caption">
    <h1>Electrical Company Providing Services</h1>
    <p>Lorem Ipsum Is Simply Dummy Text of The Printing.</p>
    <span class="btn">Read More</span>
  </div>
</section>
<div class="dots" style="top:738px"><i></i><i></i><i></i></div>

<section class="abs about">
  <h2>ABOUT US</h2>
  <div class="rule"></div>
  <div class="copy">
    Lorem Ipsum is simply dummy text of the printing and typesetting industry. Lorem Ipsum has been the industry's standard dummy text ever since the 1500s,<br>when an unknown printer took a galley of type and scrambled it to make a type specimen book. It has survived not only five centuries, but also the leap into electronic
    <ul><li>Typesetting remaining essentially unchanged.</li><li>Remaining essentially unchanged.</li></ul>
  </div>
  <span class="btn">Read More</span>
  <div class="photo" role="img" aria-label="Hands working on colourful wiring in an electrical panel"></div>
  <div class="thumbs"><span></span><span class="on"></span><span></span><span></span><span></span></div>
</section>

<section class="abs services">
  <h2 class="section-title">OUR SERVICES</h2>
  <div class="section-sub">Lorem Ipsum is simply dummy text of the printing and<br>typesetting industry.</div>
  <div class="svc-grid">
    <div class="svc">
      <svg viewBox="0 0 50 50"><path d="M14 48V8M10 48h10M14 10h30M14 10l8-6 22 6M20 10l-6 8M28 10l-6 8M36 10l-6 8M40 10v14" stroke="#0d5a9e" stroke-width="3" fill="none"/><rect x="36" y="24" width="8" height="7" fill="#0d5a9e"/></svg>
      <h3>CONSTRUCTION BUILDINGS</h3><p>Lorem Ipsum Is Simply Dummy<br>Of The Printing And Industry.</p><div class="more">Read More..◎</div>
    </div>
    <div class="svc hl">
      <svg viewBox="0 0 50 50"><path d="M5 24 25 6l20 18" stroke="#0d5a9e" stroke-width="4" fill="none"/><path d="M11 22v24h28V22L25 10z" fill="#0d5a9e"/><rect x="21" y="32" width="8" height="14" fill="#fff"/></svg>
      <h3>SINGLE STORY</h3><p>Lorem Ipsum Is Simply Dummy<br>Of The Printing And Industry.</p><div class="more">Read More..◎</div>
    </div>
    <div class="svc">
      <svg viewBox="0 0 50 50"><path d="M8 16 25 4l17 12v30H8z" fill="#0d5a9e"/><rect x="15" y="18" width="7" height="7" fill="#fff"/><rect x="28" y="18" width="7" height="7" fill="#fff"/><rect x="15" y="30" width="7" height="7" fill="#fff"/><rect x="28" y="30" width="7" height="16" fill="#fff"/></svg>
      <h3>DOUBLE STORY</h3><p>Lorem Ipsum Is Simply Dummy<br>Of The Printing And Industry.</p><div class="more">Read More..◎</div>
    </div>
    <div class="svc">
      <svg viewBox="0 0 50 50"><rect x="6" y="10" width="26" height="18" rx="2" stroke="#0d5a9e" stroke-width="3" fill="none"/><path d="M14 34h10M19 28v6" stroke="#0d5a9e" stroke-width="3"/><rect x="34" y="6" width="10" height="38" fill="#0d5a9e"/><path d="M4 44h42" stroke="#0d5a9e" stroke-width="3"/></svg>
      <h3>OFFICE FIT OUTS</h3><p>Lorem Ipsum Is Simply Dummy<br>Of The Printing And Industry.</p><div class="more">Read More..◎</div>
    </div>
    <div class="svc">
      <svg viewBox="0 0 50 50"><rect x="10" y="4" width="30" height="42" fill="#0d5a9e"/><g fill="#fff"><rect x="15" y="9" width="6" height="6"/><rect x="29" y="9" width="6" height="6"/><rect x="15" y="20" width="6" height="6"/><rect x="29" y="20" width="6" height="6"/><rect x="22" y="34" width="6" height="12"/></g></svg>
      <h3>COMMERCIAL FACTORY</h3><p>Lorem Ipsum Is Simply Dummy<br>Of The Printing And Industry.</p><div class="more">Read More..◎</div>
    </div>
    <div class="svc">
      <svg viewBox="0 0 50 50"><path d="M30 6l14 14-8 8-14-14z" fill="#0d5a9e"/><path d="M36 4l-4 6M46 14l-6 4" stroke="#0d5a9e" stroke-width="3"/><path d="M24 22 8 38l4 4 16-16" stroke="#0d5a9e" stroke-width="4" fill="none"/><path d="M4 46l6-6" stroke="#0d5a9e" stroke-width="3"/></svg>
      <h3>INSTALLATIONS</h3><p>Lorem Ipsum Is Simply Dummy<br>Of The Printing And Industry.</p><div class="more">Read More..◎</div>
    </div>
  </div>
  <div class="center-btn"><span class="btn">View More</span></div>
</section>

<section class="abs benefits">
  <h2>Benefits of Electrician</h2>
  <h4>Fast Election Services</h4>
  <p>Lorem Ipsum is simply dummy text of the printing and typesetting industry. Lorem Ipsum has been the industry's standard dummy text ever since the 1500s,<br>when an unknown printer took a galley of type and scrambled it to make a type specimen book. It has survived not only five centuries, but also the leap into electronic</p>
  <span class="btn">View More</span>
  <div class="photo" role="img" aria-label="Multimeter, screwdriver and pliers on an electrical plan"></div>
</section>

<section class="abs testimonials">
  <h2 class="section-title">CUSTOMER TESTIMONIALS</h2>
  <div class="section-sub">Lorem Ipsum is simply dummy text.</div>
  <div class="card" style="left:130px;top:175px;width:270px;height:275px">
    <div class="avatar" role="img" aria-label="Portrait of Richard John"></div>
    <h5>RICHARD JOHN</h5><div class="role">Director</div>
    <div class="quote"><b style="left:22px;top:4px">“</b>Lorem Ipsum is simply dummy text of the printing and typesetting Lorem Ipsum industry.<b style="right:22px;bottom:-18px">”</b></div>
    <div class="more">Read More..◎</div>
  </div>
  <div class="card" style="left:435px;top:160px;width:330px;height:310px;background:#fff">
    <div class="avatar" style="width:104px;height:104px" role="img" aria-label="Portrait of Richard John"></div>
    <h5>RICHARD JOHN</h5><div class="role">Creative Director</div>
    <div class="quote" style="font-size:13px;line-height:16px"><b style="left:24px;top:6px">“</b>Lorem Ipsum is simply dummy text of the printing and typesetting Lorem Ipsum industry.<b style="right:24px;bottom:-20px">”</b></div>
    <div class="more">Read More..◎</div>
  </div>
  <div class="card" style="left:800px;top:175px;width:270px;height:275px">
    <div class="avatar" role="img" aria-label="Portrait of Richard John"></div>
    <h5>RICHARD JOHN</h5><div class="role">Creative Manager</div>
    <div class="quote"><b style="left:22px;top:4px">“</b>Lorem Ipsum is simply dummy text of the printing and typesetting Lorem Ipsum industry.<b style="right:22px;bottom:-18px">”</b></div>
    <div class="more">Read More..◎</div>
  </div>
  <div class="dots"><i class="dim"></i><i></i><i class="dim"></i></div>
  <div class="center-btn"><span class="btn">View More</span></div>
</section>

<section class="abs blogs">
  <h2 class="section-title">OUR BLOGS</h2>
  <div class="section-sub">Lorem Ipsum is simply dummy text.</div>
  <article class="post" style="left:116px">
    <div class="img" role="img" aria-label="Construction workers on a building site" style="background:linear-gradient(180deg,#c9d2da,#8b8f93 55%,#6a6560)"><div class="date">01<br>Oct</div></div>
    <h6>BLOG POST TITLE</h6>
    <div class="meta"><span>▣ February 05, 2018</span><span>◉ 26 &nbsp; ♡ 12</span></div>
    <p>Lorem Ipsum is simply dummy text of the And printing matter and typesetting industry.</p>
    <div class="more">Read More...◎</div>
  </article>
  <article class="post" style="left:446px">
    <div class="img" role="img" aria-label="Modern commercial office building" style="background:linear-gradient(180deg,#aebfcd,#6f7a83 55%,#9a9c9c)"><div class="date">01<br>Oct</div></div>
    <h6>One of the Best Resorts</h6>
    <div class="meta"><span>▣ February 06, 2018</span><span>◉ 20 &nbsp; ♡ 12</span></div>
    <p>Lorem Ipsum is simply dummy text of the printing and typesetting industry.</p>
    <div class="more">Read More...◎</div>
  </article>
  <article class="post" style="left:776px">
    <div class="img" role="img" aria-label="New double storey house under a cloudy sky" style="background:linear-gradient(180deg,#dfe3e6,#8a8d90 55%,#55585b)"><div class="date">01<br>Oct</div></div>
    <h6>One of the Best Resorts In Rasia</h6>
    <div class="meta"><span>▣ February 07, 2018</span><span>◉ 26 &nbsp; ♡ 12</span></div>
    <p>Lorem Ipsum is simply dummy text of the printing and typesetting industry.</p>
    <div class="more">Read More...◎</div>
  </article>
  <div class="center-btn"><span class="btn">View More</span></div>
</section>

<section class="abs team">
  <h2 class="section-title">OUR TEAM</h2>
  <div class="member" style="left:105px"><div class="img" role="img" aria-label="Andrew, electrician with tool belt"></div><h5>Andrew</h5><div class="role">Electronics Engineering</div><div class="social"><i></i><i></i><i></i><i></i></div></div>
  <div class="member" style="left:370px"><div class="img" role="img" aria-label="Christopher, electrician in hard hat"></div><h5>Christopher</h5><div class="role">Electric Engineering</div><div class="social"><i></i><i></i><i></i><i></i></div></div>
  <div class="member" style="left:635px"><div class="img" role="img" aria-label="Felix Dumont, electrician in hard hat"></div><h5>Felix Dumont</h5><div class="role">Electric Engineering</div><div class="social"><i></i><i></i><i></i><i></i></div></div>
  <div class="member" style="left:900px"><div class="img" role="img" aria-label="Jonathon, electrician with tool belt"></div><h5>Jonathon</h5><div class="role">Operation Manager</div><div class="social"><i></i><i></i><i></i><i></i></div></div>
  <div class="center-btn"><span class="btn">View More</span></div>
</section>

<section class="abs newsletter">
  <h2 class="section-title">SUBSCRIBE TO OUR NEWSLETTER</h2>
  <div class="section-sub">TO RECEIVE THE LATEST NEWS &amp; UPDATE</div>
  <form><div class="field">Your Email</div><div class="submit">SUBMIT</div></form>
</section>

<footer class="abs footer">
  <div class="abs brand">
    <div class="mark"></div>
    <div class="name">RTV ELECTRICAL GROUP</div>
  </div>
  <div class="tag">Lorem Ipsum is simply dummy text of the printing.</div>
  <div class="social"><i></i><i></i><i></i><i></i><i></i><i></i></div>
  <div class="fcol" style="left:75px">
    <div class="ic"><svg width="16" height="20" viewBox="0 0 16 20"><path d="M8 0C3.6 0 0 3.5 0 7.8 0 13.5 8 20 8 20s8-6.5 8-12.2C16 3.5 12.4 0 8 0z" fill="#363636"/><circle cx="8" cy="7.8" r="3" fill="#fff"/></svg></div>
    <h6>ADRESS</h6><p>123 Address, Sydney, Australia</p>
  </div>
  <div class="fcol" style="left:450px">
    <div class="ic"><svg width="18" height="18" viewBox="0 0 24 24"><path d="M6.6 10.8a15.1 15.1 0 0 0 6.6 6.6l2.2-2.2c.3-.3.7-.4 1-.2 1.1.4 2.3.6 3.6.6.6 0 1 .4 1 1V20c0 .6-.4 1-1 1A17 17 0 0 1 3 4c0-.6.4-1 1-1h3.5c.6 0 1 .4 1 1 0 1.3.2 2.5.6 3.6.1.3 0 .7-.2 1z" fill="#363636"/></svg></div>
    <h6>PHONE</h6><p>+123-456-789</p>
  </div>
  <div class="fcol" style="left:825px">
    <div class="ic"><svg width="20" height="14" viewBox="0 0 20 14"><rect width="20" height="14" rx="1" fill="#363636"/><path d="M1 1l9 7 9-7" stroke="#fff" stroke-width="1.6" fill="none"/></svg></div>
    <h6>EMAIL</h6><p>info@rtvelectronic.example.com</p>
  </div>
</footer>

<div class="abs bottombar">
  <div class="legal">Privacy policy - Legal mentions - Terms and Conditions</div>
  <div class="chat">LIVE CHAT</div>
</div>

</body>
</html>
```